Tillwave - New Payment App for Student

Till-wave - A Payment App for student to make payment, track own expenses and practice good dietary habits. The App theme is Fun and excitement.
Target User: Secondary Student aged 13-18
Look and Feel: Fun, excitement and simple.
Screen 1
Login to the app using thumbprints or password
Screen 2
Display the balance
Wallet balance >>> go to screen 3 to display transaction history
Gamification balance - points + badges >>> go to screen 3
Button to make payment
Screen 2-1
Allow them to do payment
Click “Pay”
Display QR code
scanning by merchant
Payment made
Notification received
The transaction history will be shown up
Screen 2-2
Allow them to top up (alternatively to parent Top-up using credit card)
Click “Top Up”
Display QR code
Pass the cash to merchant
scanning by merchant
Payment made
Notification received
The new balance will be shown up
Screen 3
Display more details on transaction history
Payment history + gamification history (gain/redeem points)
E.g. 14 Nov Canteen purchase $5.40
- Banana +30 points
- Milk +10 points
Screen 4 (play a game to earn point)
Introduce some trivial games (while waiting in line at cafeteria or school store) to gain some points
Crosswords
Puzzle
Screen 5 (Display achievements)
Leaderboard
Where the individual stands in the class
Where the class stands overall in school
Badges
Level
Achievements
For more, please go to our website http://www.tillwave.example/
Updates
Target Market(s)
Secondary School Student aged 13-18
Industry/Entity Type
Education
Logo Text
tillwave
Look and feel

```html
<!DOCTYPE html>
<html lang="en">
<head>
<meta charset="UTF-8">
<title>Tillwave – Login</title>
<link href="https://fonts.googleapis.com/css2?family=Raleway:wght@300;400&family=Roboto:wght@300;400&display=swap" rel="stylesheet">
<style>
  :root {
    --page-bg: #f2f3f4;
    --screen-bg: #2a3e44;
    --screen-bg-deep: #243539;
    --accent: #6fd392;
    --text: #ffffff;
    --text-soft: rgba(255,255,255,0.78);
    --money-light: #6b7a3c;
    --money-dark: #2e3a22;
  }
  * { box-sizing: border-box; margin: 0; padding: 0; }
  html, body {
    width: 1200px; height: 1200px; overflow: hidden;
    background: var(--page-bg);
    font-family: "Roboto", Arial, sans-serif;
  }
  .screen {
    position: absolute; left: 300px; top: 66px;
    width: 600px; height: 1068px;
    background: linear-gradient(180deg, var(--screen-bg) 0%, var(--screen-bg-deep) 100%);
    overflow: hidden; color: var(--text);
  }
  .hero-art {
    position: absolute; left: 150px; top: 150px; width: 520px; height: 640px;
    background: radial-gradient(ellipse at 60% 40%, var(--money-light) 0%, rgba(78,92,46,0.75) 35%, rgba(46,58,34,0.35) 60%, rgba(42,62,68,0) 75%);
    transform: rotate(-20deg);
  }
  .close-btn { position: absolute; left: 44px; top: 118px; width: 40px; height: 40px; }
  .brand {
    position: absolute; left: 0; right: 0; top: 110px; text-align: center;
    font-family: "Raleway", Arial, sans-serif; font-weight: 300;
    font-size: 48px; letter-spacing: 6px;
  }
  .field {
    position: absolute; left: 110px; width: 380px; height: 60px;
  }
  .field-label {
    position: absolute; left: 0; right: 0; top: 0; text-align: center;
    font-size: 30px; font-weight: 300; color: var(--text-soft);
  }
  .field-line {
    position: absolute; left: 6px; right: 6px; bottom: 6px; height: 2px; background: var(--accent);
  }
  .field-line::before, .field-line::after {
    content: ""; position: absolute; top: -5px; width: 12px; height: 12px; border-radius: 50%; background: var(--accent);
  }
  .field-line::before { left: -6px; }
  .field-line::after { right: -6px; }
  .field-username { top: 330px; }
  .field-password { top: 430px; }
  .forgot-link {
    position: absolute; left: 0; right: 0; top: 520px; text-align: center;
    font-size: 20px; font-weight: 300; color: var(--text-soft);
  }
  .login-btn {
    position: absolute; left: 130px; top: 610px; width: 340px; height: 90px;
    border: 2px solid var(--accent); border-radius: 6px; background: transparent;
    color: var(--text); font-family: inherit; font-size: 32px; font-weight: 400;
  }
  .thumbprint { position: absolute; left: 255px; top: 820px; width: 90px; height: 100px; }
  .thumbprint-label {
    position: absolute; left: 0; right: 0; top: 940px; text-align: center;
    font-size: 26px; font-weight: 300;
  }
</style>
</head>
<body>
<main class="screen">
  <div class="hero-art" role="img" aria-label="Illustration of bundles of banknotes flying out of an open briefcase"></div>

  <svg class="close-btn" viewBox="0 0 40 40" aria-label="Close">
    <path d="M4 4 L36 36 M36 4 L4 36" stroke="#ffffff" stroke-width="2.5" fill="none"/>
  </svg>
  <h1 class="brand">Tillwave</h1>

  <div class="field field-username">
    <span class="field-label">Username</span>
    <span class="field-line"></span>
  </div>
  <div class="field field-password">
    <span class="field-label">Password</span>
    <span class="field-line"></span>
  </div>
  <p class="forgot-link">Forgot your username/password?</p>

  <button class="login-btn">Login</button>

  <svg class="thumbprint" viewBox="0 0 90 100" aria-label="Thumbprint icon" fill="none" stroke="#ffffff" stroke-width="3" stroke-linecap="round">
    <path d="M10 40 A35 35 0 0 1 80 40"/>
    <path d="M6 60 C4 30 30 10 45 10"/>
    <path d="M18 80 C10 60 14 22 45 22 C72 22 78 50 74 74"/>
    <path d="M28 90 C18 70 22 34 45 34 C64 34 66 56 64 84"/>
    <path d="M38 96 C28 74 32 46 45 46 C56 46 56 66 54 92"/>
    <path d="M45 58 C44 72 46 86 48 98"/>
    <path d="M84 60 C86 70 84 80 82 88"/>
  </svg>
  <p class="thumbprint-label">Thumbprint for Login</p>
</main>
</body>
</html>
```